Graphic Design for our Marlow Vans

Creative Vehicle Branding & Van Wrap Design – RFP
Oakridge Fieldworks Inc. (OFI) is seeking a creative, innovative designer or agency to develop a new, standout branding design for our four Halvern Marlow service vans.
This design must reflect who we are and what we do: electrical service, construction, and large-scale commercial, roadway, and sports lighting. This is a company that works in the air, not behind a desk.
The Objective
Create a highly recognizable, eye-catching van design that:
Clearly communicates electrical and lighting expertise
Reflects scale, capability, and professionalism
Stands out on highways, job sites, and parking lots
Feels bold and modern, not generic contractor stock art
Our vans are rolling billboards for serious infrastructure work. They should look the part.
Critical Context (Read This Carefully)
Most of our work is performed from bucket trucks
We operate bucket trucks reaching up to 140 feet
Our crews work on:
Street and roadway lighting
Sports field lighting
Commercial and industrial lighting
Electrical service and construction
The design should acknowledge verticality, height, light, and scale.
That could mean visual elements that imply:
Reaching upward
Light projection
Infrastructure
Power, precision, and access
Literal illustrations are not required, but the design should feel relevant to high-reach, high-visibility work.
Non-Negotiables
The existing OFI logo stays exactly as-is
No redesigns, distortions, or reinterpretations of the logo
Everything else is open for exploration
Creative Freedom (Encouraged)
You may explore:
Bold color systems
High-contrast layouts
Clean, strong typography (outside the logo)
Abstract or graphic representations of light, elevation, or power
Minimal but impactful messaging
If it looks like every other electrical contractor van, we’re not interested.
Design Requirements
Eye-catching at speed and from distance
Clean and professional up close
Scalable across four vans and future fleet growth
Practical for real-world wrap production
Timeless enough to last, modern enough to matter
Scope of Work
Concept development (multiple design directions preferred)
Final wrap-ready design files for Halvern Marlow vans
Layout consideration for sides, rear, and doors
Coordination-friendly designs for professional wrap installation
Who Should Respond
Designers or agencies with vehicle wrap or large-format branding experience
Strong conceptual thinkers who design with intent
Comfortable working with construction, electrical, or infrastructure brands
Willing to push ideas and explain the reasoning behind them
How to Respond
Please include:
Relevant portfolio examples (vehicle wraps strongly preferred)
Your creative approach and thinking process
Estimated timeline
Pricing structure
Any early concepts or ideas (optional but welcome)
We’re looking for a design that reflects scale, capability, and confidence.
This should look like a company that works at 140 feet in the air and knows exactly what it’s doing.

```html
<!DOCTYPE html>
<html lang="en">
<head>
<meta charset="utf-8">
<title>Oakridge Fieldworks Inc. – Halvern Marlow Van Wrap</title>
<link rel="stylesheet" href="https://fonts.googleapis.com/css2?family=Nunito+Sans:wght@600;700;800;900&display=swap">
<style>
  :root {
    --wrap-red: #d0152b;
    --wrap-blue: #1c2a9c;
    --wrap-white: #fbfbfc;
    --trim-black: #1b1d22;
    --glass: #2b3038;
    --tyre: #202226;
    --hub: #b9bcc1;
    --backdrop: #e9eaec;
  }
  html, body {
    margin: 0;
    padding: 0;
    width: 1200px;
    height: 1185px;
    overflow: hidden;
    background: var(--backdrop);
  }
  .wrap-sheet {
    display: block;
    width: 1200px;
    height: 1185px;
    font-family: "Nunito Sans", Arial, sans-serif;
  }
  .body-panel { fill: var(--wrap-white); stroke: #c9ccd1; stroke-width: 2; }
  .red-field { fill: var(--wrap-red); }
  .blue-stripe { fill: var(--wrap-blue); }
  .lower-band { fill: var(--trim-black); }
  .glass { fill: var(--glass); }
  .tyre { fill: var(--tyre); }
  .hub { fill: var(--hub); }
  .company-name { fill: var(--wrap-red); font-weight: 800; }
  .web-address { fill: var(--wrap-red); font-weight: 700; font-size: 32px; }
  .service-list { fill: #ffffff; font-weight: 700; font-size: 21px; }
  .phone-number { fill: #ffffff; font-weight: 700; font-size: 44px; }
</style>
</head>
<body>
<svg class="wrap-sheet" viewBox="0 0 1500 1481" xmlns="http://www.w3.org/2000/svg" role="img" aria-label="Van wrap design, driver and passenger sides">
  <defs>
    <clipPath id="van-outline">
      <path d="M95,480 C100,440 140,410 210,385 L330,270 C380,200 450,150 560,120 L1340,105 C1375,105 1385,120 1390,160 L1405,470 L1420,500 L1420,585 L80,590 L78,510 Z"/>
    </clipPath>
    <g id="van-side">
      <path class="body-panel" d="M95,480 C100,440 140,410 210,385 L330,270 C380,200 450,150 560,120 L1340,105 C1375,105 1385,120 1390,160 L1405,470 L1420,500 L1420,585 L80,590 L78,510 Z"/>
      <g clip-path="url(#van-outline)">
        <path class="red-field" d="M1030,90 C1115,180 1135,360 945,500 L1450,500 L1450,90 Z"/>
        <path class="blue-stripe" d="M1005,90 C1095,180 1112,365 918,500 L945,500 C1135,360 1115,180 1030,90 Z"/>
        <path class="red-field" d="M885,492 C940,470 975,445 1005,415 C985,450 950,478 905,495 Z"/>
        <rect class="lower-band" x="60" y="495" width="1380" height="100"/>
        <polygon class="red-field" points="600,575 800,543 948,543 948,575"/>
        <polygon class="blue-stripe" points="790,575 850,543 862,543 802,575"/>
        <polygon points="370,575 600,575 800,543 370,548" fill="#ffffff"/>
      </g>
      <path class="glass" d="M120,440 C150,410 185,395 205,392 L170,425 C150,432 130,440 120,440 Z"/>
      <path class="glass" d="M235,410 L335,285 C360,255 385,245 410,242 L395,395 L300,398 Z"/>
      <path class="glass" d="M418,242 L505,240 L505,388 L402,392 Z"/>
      <circle class="tyre" cx="265" cy="580" r="72"/>
      <circle class="hub" cx="265" cy="580" r="36"/>
      <circle class="tyre" cx="1040" cy="585" r="72"/>
      <circle class="hub" cx="1040" cy="585" r="36"/>
    </g>
  </defs>

  <!-- Driver side (cab facing left) -->
  <g class="van van--driver-side">
    <use href="#van-side"/>
    <text class="company-name" x="780" y="262" font-size="82" text-anchor="middle">OAKRIDGE</text>
    <text class="company-name" x="780" y="340" font-size="70" text-anchor="middle">FIELDWORKS</text>
    <text class="company-name" x="778" y="372" font-size="30" text-anchor="middle">INCORPORATED</text>
    <text class="web-address" x="542" y="447">oakridgefieldworks.com</text>
    <g class="service-list">
      <text x="1138" y="175">• Electrical</text>
      <text x="1138" y="208">• Commercial Lighting</text>
      <text x="1138" y="240">• Traffic Signal</text>
      <text x="1138" y="273">• Directional Drilling</text>
      <text x="1138" y="305">• Signs</text>
      <text x="1138" y="338">• Sports Lighting</text>
      <text x="1138" y="370">• Utilities</text>
      <text x="1138" y="403">• Roadway Lighting</text>
    </g>
    <text class="phone-number" x="1045" y="463">(877) 555-0142</text>
  </g>

  <!-- Passenger side (cab facing right) -->
  <g class="van van--passenger-side">
    <use href="#van-side" transform="translate(1500,722) scale(-1,1)"/>
    <text class="company-name" x="735" y="980" font-size="82" text-anchor="middle">OAKRIDGE</text>
    <text class="company-name" x="735" y="1058" font-size="70" text-anchor="middle">FIELDWORKS</text>
    <text class="company-name" x="733" y="1092" font-size="30" text-anchor="middle">INCORPORATED</text>
    <text class="web-address" x="770" y="1170" text-anchor="middle">oakridgefieldworks.com</text>
    <g class="service-list" text-anchor="end">
      <text x="367" y="890">Electrical •</text>
      <text x="367" y="924">Commercial Lighting •</text>
      <text x="367" y="958">Traffic Signal •</text>
      <text x="367" y="991">Directional Drilling •</text>
      <text x="367" y="1025">Signs •</text>
      <text x="367" y="1058">Sports Lighting •</text>
      <text x="367" y="1092">Utilities •</text>
      <text x="367" y="1125">Roadway Lighting •</text>
    </g>
    <text class="phone-number" x="152" y="1187">(877) 555-0142</text>
  </g>
</svg>
</body>
</html>
```